Wedding Planning and Event Planners website

I am driven by perfection of my occupation and i look forward to having an attractive and contemporary website for an event and wedding planning group. We are located in the United States and Canada and we offer our services only in these two countries. My website is for people who are planning events such Church programs, weddings, musical concerts, Picnic, etc. My website should have imaginary of events such as weddings, musical concerts and picnic, etc.. I don't have any reference website because i want all designers to be creative and unique. I prefer blue,red,green,yellow colors.

Industry/Entity Type

Wedding

Coding

Coded - Design and coding required

```html
<!DOCTYPE html>
<html lang="en">
<head>
<meta charset="utf-8">
<title>Evermore Events</title>
<link href="https://fonts.googleapis.com/css2?family=Cabin:wght@400;500;600;700&family=Open+Sans:wght@400;600&display=swap" rel="stylesheet">
<style>
:root{
  --green:#6aae12;
  --green-dark:#4f8a0a;
  --yellow:#e3dc06;
  --dark:#1b1b1b;
  --charcoal:#333333;
  --text:#333333;
  --muted:#8a8a8a;
  --light:#f4f4f4;
  --white:#ffffff;
}
*{box-sizing:border-box;margin:0;padding:0}
html,body{width:1200px;height:3789px;overflow:hidden;background:var(--white)}
body{position:relative;font-family:'Open Sans',sans-serif;color:var(--text)}
.abs{position:absolute}
a{color:inherit;text-decoration:none}

/* header */
.header{left:0;top:0;width:1200px;height:134px;background:var(--white)}
.logo{left:60px;top:26px;font-family:'Cabin',sans-serif;font-weight:600;font-size:38px;line-height:40px;color:var(--dark);letter-spacing:1px}
.call{left:589px;top:20px;display:flex;align-items:center;gap:10px}
.call small{display:block;font-size:12px;color:var(--dark);line-height:13px}
.call strong{display:block;font-family:'Cabin',sans-serif;font-size:20px;line-height:22px;color:var(--dark)}
.btn{display:flex;align-items:center;justify-content:center;font-family:'Cabin',sans-serif;font-weight:600;font-size:17px;border-radius:3px}
.btn-book{left:740px;top:15px;width:152px;height:41px;background:var(--yellow);color:var(--dark)}
.btn-enquiry{left:904px;top:15px;width:152px;height:41px;background:var(--charcoal);color:var(--white)}
.socials{left:1072px;top:29px;display:flex;gap:10px}
.socials span{width:13px;height:13px;border-radius:50%;background:var(--green)}
.nav{left:493px;top:76px;display:flex;height:38px}
.nav a{display:flex;align-items:center;padding:0 16px;font-family:'Cabin',sans-serif;font-weight:500;font-size:15px;color:var(--dark)}
.nav a.active{background:var(--green);color:var(--white);padding:0 20px}

/* hero */
.hero-photo{left:0;top:134px;width:644px;height:553px;background:radial-gradient(circle at 25% 30%,#f2f3ea 0,#c9c9b5 30%,#8a7a55 60%,#5a4a2c 100%)}
.hero-panel{left:644px;top:134px;width:556px;height:553px;background:linear-gradient(135deg,#3a3a3a,#151515)}
.hero-title{left:715px;top:250px;font-family:'Cabin',sans-serif;font-weight:600;font-size:30px;line-height:40px;color:var(--white);letter-spacing:.5px}
.field{background:#bfbfbf;border:1px solid #e0e0e0;border-radius:3px;color:var(--dark);font-size:14px;padding-left:14px;display:flex;align-items:center;height:40px}
.f-type{left:715px;top:354px;width:354px}
.f-name{left:715px;top:412px;width:172px}
.f-phone{left:900px;top:412px;width:169px}
.f-date{left:715px;top:470px;width:172px}
.f-time{left:900px;top:470px;width:169px}
.btn-submit{left:715px;top:528px;width:354px;height:43px;background:var(--yellow);color:var(--dark)}

/* welcome */
.section-title{left:0;width:1200px;text-align:center;font-family:'Cabin',sans-serif;font-weight:500;font-size:36px;color:var(--dark)}
.welcome-title{top:784px}
.welcome-text{left:150px;top:856px;width:900px;text-align:center;font-size:12px;line-height:21px;color:var(--muted)}
.btn-more{left:455px;top:1000px;width:146px;height:43px;background:var(--green);color:var(--white)}
.btn-join{left:621px;top:1000px;width:144px;height:43px;background:var(--yellow);color:var(--dark)}

/* offering */
.offer-band{left:0;top:1152px;width:1200px;height:662px;background:linear-gradient(180deg,#7cb52a 0%,#69a81a 50%,#5b9a12 100%)}
.offer-title{top:1214px;color:var(--white)}
.rule{width:56px;height:4px;background:var(--yellow);left:572px}
.card{width:290px;background:var(--white)}
.card-photo{position:absolute;left:0;top:0;width:290px;height:225px}
.card-label{position:absolute;left:27px;top:207px;width:236px;height:38px;background:var(--yellow);display:flex;align-items:center;justify-content:center;font-family:'Cabin',sans-serif;font-weight:600;font-size:16px;color:var(--dark)}
.card-text{position:absolute;left:25px;top:262px;width:240px;text-align:center;font-size:13px;line-height:21px;color:#555}

/* events */
.events-title{top:1916px}
.tile{position:absolute}
.feature-box{left:129px;top:2117px;width:475px;height:258px;background:rgba(227,220,6,.82);padding:34px 30px 0}
.feature-box h3{font-family:'Cabin',sans-serif;font-weight:600;font-size:28px;color:var(--dark);text-align:center}
.feature-box p{font-size:13px;line-height:20px;color:var(--dark);text-align:center;margin-top:14px}
.feature-box time{position:absolute;right:26px;bottom:20px;font-size:14px;font-weight:600;color:var(--dark)}

/* testimonials */
.clients-band{left:0;top:2804px;width:1200px;height:560px;background:var(--light)}
.clients-title{top:2881px}
.quote{width:290px;height:283px;background:var(--white);text-align:center}
.quote h4{margin-top:34px;font-family:'Cabin',sans-serif;font-weight:500;font-size:19px;color:var(--dark)}
.avatar{width:104px;height:104px;border-radius:50%;border:5px solid var(--green);margin:16px auto 0;background:linear-gradient(135deg,#e8e8e8,#bcbcbc)}
.quote p{width:240px;margin:14px auto 0;font-size:13px;line-height:21px;color:#555}

/* footer */
.footer{left:0;top:3364px;width:1200px;height:375px;background:#111}
.f-logo{left:61px;top:3410px;font-family:'Cabin',sans-serif;font-weight:600;font-size:34px;line-height:36px;color:var(--white);letter-spacing:1px}
.f-about{left:61px;top:3506px;width:300px;font-size:13px;line-height:23px;color:#ddd}
.f-social{left:61px;top:3681px;display:flex;gap:15px}
.f-social span{width:14px;height:14px;border-radius:50%;background:var(--white)}
.f-head{font-family:'Cabin',sans-serif;font-weight:600;font-size:18px;color:var(--white);display:flex;align-items:center;gap:16px}
.f-head::after{content:"";height:1px;background:#555;width:170px}
.f-info-head{left:488px;top:3421px}
.f-office-head{left:866px;top:3421px}
.f-links{display:flex;flex-direction:column;gap:14px;font-size:13px;color:#ddd}
.f-links li{list-style:none;line-height:21px}
.f-links li::before{content:"›";margin-right:10px}
.f-office{left:866px;top:3508px;display:flex;flex-direction:column;gap:10px;font-size:13px;color:#ddd}
.f-office div{display:flex;align-items:center;gap:12px;height:25px}
.copyright{left:0;top:3739px;width:1200px;height:50px;background:#2b2b2b;display:flex;align-items:center;justify-content:center;font-size:12px;color:#aaa}
</style>
</head>
<body>

<header class="abs header">
  <div class="abs logo">EVERMORE<br>EVENTS</div>
  <div class="abs call">
    <svg width="22" height="22" viewBox="0 0 24 24"><circle cx="12" cy="12" r="11" fill="#1b1b1b"/><path d="M8 6.5l2 2-1 1.5c.8 1.7 2.3 3.2 4 4l1.5-1 2 2-1.5 2c-3.5-.3-7.2-4-7.5-7.5z" fill="#fff"/></svg>
    <div><small>Call us</small><strong>555 0142 77</strong></div>
  </div>
  <a class="abs btn btn-book">Book your event</a>
  <a class="abs btn btn-enquiry">Enquiry us</a>
  <div class="abs socials"><span></span><span></span><span></span></div>
  <nav class="abs nav">
    <a class="active">HOME</a><a>ABOUT US</a><a>EVENTS</a><a>FAQS</a><a>BOOK EVENT</a><a>GALLERY</a><a>CONTACT US</a>
  </nav>
</header>

<section>
  <div class="abs hero-photo" role="img" aria-label="White flower centrepiece and wine glasses on a reception table"></div>
  <div class="abs hero-panel" role="img" aria-label="Dimmed photo of glassware on a dark table"></div>
  <h1 class="abs hero-title">MAKE YOUR EVENTS BEST<br>MORE MEMORABLE</h1>
  <div class="abs field f-type">Event type</div>
  <div class="abs field f-name">Your name</div>
  <div class="abs field f-phone">Your Phone no</div>
  <div class="abs field f-date">Select Event date</div>
  <div class="abs field f-time">Select Event time</div>
  <a class="abs btn btn-submit">Book your beautiful event with us</a>
</section>

<section>
  <h2 class="abs section-title welcome-title">Welcome to Event Management</h2>
  <p class="abs welcome-text">We plan weddings, church programs, concerts and picnics across the United States and Canada, taking care of every detail from the first idea to the final toast. Our team handles venues, decor, catering, music, guest lists and timing so you can simply enjoy the day with the people you love. Every celebration is shaped around your story, your style and your budget, with clear planning and honest advice at each step. Tell us what you imagine and we will bring it together with care, calm and a little magic.</p>
  <a class="abs btn btn-more">Know More</a>
  <a class="abs btn btn-join">Join us</a>
</section>

<section>
  <div class="abs offer-band" role="img" aria-label="Green-tinted photo of an outdoor reception with rows of chairs"></div>
  <h2 class="abs section-title offer-title">WE OFFERING YOU</h2>
  <div class="abs rule" style="top:1268px"></div>

  <div class="abs card" style="left:61px;top:1316px;height:389px">
    <div class="card-photo" role="img" aria-label="Bride and groom standing together at a wedding" style="background:linear-gradient(180deg,#f2f2ef,#c9cfd4)"></div>
    <div class="card-label">Wedding Event Planning</div>
    <p class="card-text">Ceremony, reception and every detail in between, planned around your day.</p>
  </div>
  <div class="abs card" style="left:455px;top:1316px;height:389px">
    <div class="card-photo" role="img" aria-label="Guitarist performing on stage under colourful lights" style="background:radial-gradient(circle at 50% 45%,#e8893a 0,#a8352a 35%,#2a1030 100%)"></div>
    <div class="card-label">Music consert Planning</div>
    <p class="card-text">Stage, sound, lights and crowd flow handled for a night to remember.</p>
  </div>
  <div class="abs card" style="left:849px;top:1316px;height:389px">
    <div class="card-photo" role="img" aria-label="Picnic tables set on a lawn under string lights" style="background:linear-gradient(180deg,#d9d5c8 0%,#a79a80 45%,#6e8a3c 100%)"></div>
    <div class="card-label">Picnic &amp; church Event</div>
    <p class="card-text">Relaxed outdoor gatherings and warm church programs for every community.</p>
  </div>
</section>

<section>
  <h2 class="abs section-title events-title">OUR MOST BEAUTIFUL EVENTS</h2>
  <div class="abs rule" style="top:1970px;background:var(--green)"></div>

  <div class="tile" style="left:61px;top:2041px;width:591px;height:392px;background:linear-gradient(180deg,#d8dde0 0%,#b8b6a6 45%,#8d8d83 100%)" role="img" aria-label="Beach wedding aisle with white chairs and flower petals"></div>
  <div class="tile" style="left:662px;top:2041px;width:477px;height:321px;background:linear-gradient(180deg,#e5e5e3,#b9b6b0 60%,#4a4848)" role="img" aria-label="School band rehearsing with brass instruments"></div>
  <div class="tile" style="left:662px;top:2374px;width:477px;height:319px;background:linear-gradient(180deg,#a9875a,#7a5332 55%,#4a2c18)" role="img" aria-label="Church interior with stone arches set for a dinner"></div>
  <div class="tile" style="left:61px;top:2450px;width:290px;height:243px;background:linear-gradient(180deg,#9fb5b8,#5f8740 60%,#3e6a24)" role="img" aria-label="Garden party with paper lanterns and tables"></div>
  <div class="tile" style="left:364px;top:2450px;width:288px;height:243px;background:linear-gradient(180deg,#d9dbd0,#9aa07a 55%,#6a8a3a)" role="img" aria-label="Picnic tables on a lawn beside a barn"></div>

  <div class="abs feature-box">
    <h3>Mara &amp; Leo Wedding Event</h3>
    <p>A seaside ceremony with a petal aisle, a sunset dinner and dancing under the stars with close family and friends.</p>
    <time>23 March 2015</time>
  </div>
</section>

<section>
  <div class="abs clients-band"></div>
  <h2 class="abs section-title clients-title">WHAT OUR CLIENTS SAYS</h2>
  <div class="abs rule" style="top:2934px;background:var(--green)"></div>

  <div class="abs quote" style="left:61px;top:2991px">
    <h4>Nina &amp; Paul</h4>
    <div class="avatar" role="img" aria-label="Portrait of the couple"></div>
    <p>Every detail was perfect and our guests are still talking about it.</p>
  </div>
  <div class="abs quote" style="left:455px;top:2991px">
    <h4>Grace Chapel</h4>
    <div class="avatar" role="img" aria-label="Portrait of the church organiser"></div>
    <p>Our program ran smoothly from start to finish. Thank you all.</p>
  </div>
  <div class="abs quote" style="left:849px;top:2991px">
    <h4>Owen Music Concert</h4>
    <div class="avatar" role="img" aria-label="Portrait of the concert organiser"></div>
    <p>Great sound, great crowd and zero stress on the night itself.</p>
  </div>
</section>

<footer>
  <div class="abs footer"></div>
  <div class="abs f-logo">EVERMORE<br>EVENTS</div>
  <p class="abs f-about">Evermore is created with an eye to ease your process of planning a beautiful event while at the same time, deliver a premium experience to your guests. Your celebration is flourishing, give it a complement.</p>
  <div class="abs f-social"><span></span><span></span><span></span><span></span><span></span><span></span></div>

  <div class="abs f-head f-info-head">Information</div>
  <ul class="abs f-links" style="left:488px;top:3509px"><li>About Us</li><li>Our Team</li><li>Testimonials</li><li>Our Services</li><li>Careers</li></ul>
  <ul class="abs f-links" style="left:657px;top:3509px"><li>Overview</li><li>Innovation</li><li>Who We Are</li><li>Projects</li><li>Contact Us</li></ul>

  <div class="abs f-head f-office-head">Office</div>
  <div class="abs f-office">
    <div><svg width="12" height="14" viewBox="0 0 12 14"><path d="M6 0a5 5 0 0 0-5 5c0 4 5 9 5 9s5-5 5-9a5 5 0 0 0-5-5zm0 7a2 2 0 1 1 0-4 2 2 0 0 1 0 4z" fill="#ddd"/></svg>82 Maple Avenue, Portland, Oregon</div>
    <div><svg width="13" height="13" viewBox="0 0 24 24"><path d="M5 3l4 4-2 3c1.5 3 4 5.5 7 7l3-2 4 4-3 3C10 21 3 14 2 6z" fill="#ddd"/></svg>(555) 0100 2200</div>
    <div><svg width="14" height="11" viewBox="0 0 14 11"><rect x="0.5" y="0.5" width="13" height="10" fill="none" stroke="#ddd"/><path d="M1 1l6 5 6-5" fill="none" stroke="#ddd"/></svg>info@evermore-events.example</div>
    <div><svg width="14" height="11" viewBox="0 0 14 11"><rect x="0.5" y="0.5" width="13" height="10" fill="#ddd"/><rect x="2" y="3" width="10" height="1.5" fill="#111"/></svg>(555) 0100 3300</div>
    <div><svg width="13" height="13" viewBox="0 0 14 14"><circle cx="7" cy="7" r="6" fill="none" stroke="#ddd" stroke-width="1.5"/><path d="M7 3.5V7l2.5 1.5" fill="none" stroke="#ddd" stroke-width="1.5"/></svg>Mon - Sat: 9:00 - 18:00</div>
  </div>
  <div class="abs copyright">© 2016 EVERMORE EVENTS ALL RIGHT RESERVED.</div>
</footer>

</body>
</html>
```